Website for Amber Crest Dispensing LLC

I am one of 3 owners of a vending company started last year. Our business is new, but we would like to expand locally in the near future. We have created a landing page using pagemold.com, but we would like some professional help getting it updated. We want to rework our website and give it a fresh and modern feel. We would like the main page of the site to be an advertisement of our services with a small introduction of our company around the top of the page. The main goal of the site is to solicit local businesses to contact us for placement of a vending machine in their place of business.

Theme:
We have a logo for the company, so I would like the theme of the site to be based around the logo. We would like the main page of the site to be mainly dedicated to promoting and advertising our services and features. The main page should include very modern vending machines and/or mini markets in the background, with a brief introduction to our company at the top of the page.

Features to include:
Introduction of our company and an advertisement of our services - We would like the main page of the site to have a brief description of what our company is and does, how we provide quick and reliable service to our customers with a variety of snack options.
Benefits of snack services: list some of the great benefits of having a vending machine in your business
Vending Machines that we offer: we would like to present information about the variety of different machines that we offer our clients, including: traditional snack machines, drink machines, cold food machines, coffee machines, and mini markets. We have access to all of the latest and most innovative machines to meet client needs. All machines are modern and include the latest technology of tap-to-pay options. Based upon the needs of the commercial space, we offer the machines all free of charge to our clients, we do an assessment of the space and client needs to determine what model of smart-vending machine should be placed in the space
"Request a Refund": This is a tab that leads to a form on a different page dedicated to patrons of our current machine who would like to request a refund from our company because the product did not dispense or for any technical difficulty. The form should include a space for customer name, a drop down field for preferred customer contact, with the options of phone(text) or email, location of the machine, a drop-down field for which machine they used (options: drink machine, cold food machine, snack machine, or coffee machine), item number, item price, time of attempted purchase, refund amount requested, and a comment window for a description of the problem, and a drop down window of how they would like the money returned if request is approved (options: paybeam, coinlift, sendra, orchard pay, check mailed....if check mailed is chosen another window should appear requesting customer address.). When the form is submitted, we would like all information to come to our business email where we can investigate the issue and issue a refund if needed. Our business email address is ambercrestdispensing@mailnook.com. After the submit button is pressed, we would like a text(SMS) to be sent to the phone number provided, preferably from our business number(Relay Phone number (555) 271-0962) or an automatic email to be sent to their email account from our email account(ambercrestdispensing@mailnook.com)
SMS message:
"Thank you for contacting Amber Crest Dispensing. Your request has been received and is under review. A team member will be in touch within 24–48 hours."

Email message:
Subject: We’ve Received Your Request

Hi [Name],

Thank you for contacting Amber Crest Dispensing. We’ve received your request and are currently reviewing the details.

A member of our team will follow up with you within 24–48 hours to assist further.

Best regards,
Amber Crest Dispensing

"Contact us" tab - Leads to a different page with our Name, business address (Address:
Amber Crest Dispensing LLC
312 Hollowell Lane #2876
Belleville MI
49207), business phone number, and email address. With 2 fields for: name and email address, and one text box for comments. After the comment is submitted, a text on-screen message should appear that says: "Thank you for your feedback and for choosing Amber Crest Dispensing.
Your input is valuable to us and helps us continue to improve our service and customer experience."
The 'request a machine placement' button should lead to the form at the bottom of the page.. The form should also include a section for personal contact information, the Name of the business, the type of business, the business address, the type of machines requested, and an estimated amount of daily foot traffic at the placement site.

I believe this is a good start to the revamp. I have included an attachment of our logo. Please let me know if you have any questions.
Thanks in advance.

Amber Crest Dispensing

Target Market(s)

Local Businesses looking for free Vending Services

Industry/Entity Type

Vending

Coding

Coded - Design and coding required

Number of Pages Required

3 page

Colors
A7469A
B969AE
D3A5CF
EDDBEB
F8F0F9

Requirements
Must have
• a page linked to a fill-out form for customer refunds

```html
<!DOCTYPE html>
<html lang="en">
<head>
<meta charset="utf-8">
<title>Amber Crest Dispensing — Smarter Snacks for Today's Workplace</title>
<link href="https://fonts.googleapis.com/css2?family=Orbitron:wght@500;600&family=Roboto:wght@400;500;700&display=swap" rel="stylesheet">
<style>
:root{
  --pink:#ec3a8e;
  --pink-soft:#f7c6dd;
  --purple:#32194d;
  --purple-deep:#28133f;
  --lilac:#f1eef5;
  --grey:#f1f1f1;
  --ink:#1f1f2b;
  --text:#444450;
  --white:#ffffff;
}
*{box-sizing:border-box;margin:0;padding:0}
html,body{width:1200px;height:4186px;overflow:hidden;background:var(--white)}
body{font-family:"Roboto",Arial,sans-serif;color:var(--text)}
.page{position:relative;width:1200px;height:4186px;overflow:hidden}
.abs{position:absolute}
.heading{font-family:"Orbitron",Arial,sans-serif;font-weight:500;color:var(--ink);letter-spacing:1px;text-transform:uppercase}
.underline{position:absolute;height:6px;background:var(--pink);clip-path:polygon(0 0,100% 0,92% 100%,0 100%)}
.btn{position:absolute;display:flex;align-items:center;justify-content:center;background:var(--pink);color:var(--white);font-weight:700;font-size:15px;text-transform:uppercase;text-decoration:none;letter-spacing:.2px}

/* header */
.site-header{position:absolute;left:0;top:0;width:1200px;height:114px;background:var(--white)}
.brand{position:absolute;display:flex;align-items:center;gap:10px;color:var(--purple);font-weight:700;text-transform:uppercase;letter-spacing:2px;white-space:nowrap}
.brand-square{background:var(--pink);flex:none}
.nav{position:absolute;left:300px;top:85px;display:flex;gap:14px;font-size:12px;font-weight:700;color:var(--ink);text-transform:uppercase;white-space:nowrap}
.nav a{color:inherit;text-decoration:none}
.nav a.active{color:var(--pink)}
.social{position:absolute;display:flex;gap:8px}
.social span{width:30px;height:30px;border-radius:50%;background:#e8e8ec}
.social span:first-child{background:var(--pink)}
.call-box{position:absolute;left:920px;top:0;width:280px;height:114px;background:var(--purple);clip-path:polygon(60px 0,100% 0,100% 100%,0 100%)}

/* hero */
.hero-photo{position:absolute;left:0;top:114px;width:1200px;height:658px;background:linear-gradient(100deg,#b9ac9c 0%,#8d8173 28%,#4a4651 55%,#2c2a33 80%,#1e1d24 100%)}
.hero-shade{position:absolute;left:0;top:114px;width:1200px;height:658px;background:rgba(20,16,30,.35)}
.hero-title{position:absolute;left:0;top:286px;width:1200px;text-align:center;color:var(--white);font-family:"Orbitron",Arial,sans-serif;font-weight:600;font-size:43px;line-height:51px;text-transform:uppercase;letter-spacing:1px}
.hero-sub{position:absolute;left:0;top:392px;width:1200px;text-align:center;color:var(--white);font-size:19px;line-height:29px;font-weight:500}
.dots span{position:absolute;left:1117px;width:15px;height:15px;border:2px solid var(--white);border-radius:50%}
.dots span.on{background:var(--white)}

/* about */
.photo{position:absolute}
.about-text{position:absolute;left:600px;width:457px;font-size:13.5px;line-height:24px;text-align:justify;color:var(--text)}

/* machines */
.machines{position:absolute;left:0;top:1363px;width:1200px;height:718px;background:var(--lilac)}
.card{position:absolute;top:1541px;height:464px;background:var(--white);box-shadow:0 4px 14px rgba(40,20,60,.12);text-align:center;border-radius:4px}
.card.featured{border:2px solid var(--pink)}
.card .machine{position:absolute;top:36px;left:50%;transform:translateX(-50%);width:110px;height:196px;border-radius:4px}
.card h3{position:absolute;top:258px;left:0;width:100%;font-size:15.5px;font-weight:500;color:var(--ink);text-transform:uppercase}
.card p{position:absolute;top:283px;left:22px;right:22px;font-size:13.5px;line-height:22.5px;color:var(--text)}
.card .go{position:absolute;top:406px;left:50%;transform:translateX(-50%);width:32px;height:32px;border-radius:50%;background:var(--pink-soft);display:flex;align-items:center;justify-content:center}
.card.featured .go{background:var(--pink)}
.more-machines{position:absolute;left:0;top:2028px;width:1200px;display:flex;justify-content:center;align-items:center;gap:12px;font-size:13.5px;color:var(--ink)}
.more-machines strong{font-weight:700;text-transform:uppercase;font-size:13px}
.more-machines span{background:var(--white);border:1px solid var(--pink-soft);border-radius:16px;padding:6px 14px;font-weight:500}

/* benefits */
.benefits{position:absolute;left:0;top:2081px;width:1200px;height:699px;background:linear-gradient(180deg,#3a2056 0%,var(--purple) 60%,var(--purple-deep) 100%)}
.hex{position:absolute;top:2301px;width:213px;height:244px}
.hex svg.shape{position:absolute;left:0;top:0}
.hex .label{position:absolute;left:18px;right:18px;top:122px;text-align:center;font-size:14.5px;line-height:23px;font-weight:700;color:var(--ink);text-transform:uppercase}
.hex.active .label{color:var(--white)}
.hex .icon{position:absolute;left:76px;top:40px}

/* testimonials */
.quote{position:absolute;top:2902px;width:280px;height:304px;background:var(--white);box-shadow:0 3px 14px rgba(40,20,60,.12)}
.quote .stars{position:absolute;left:26px;top:25px;color:#f5a623;font-size:14px;letter-spacing:1px}
.quote p{position:absolute;left:26px;right:26px;top:52px;font-size:14px;line-height:23.3px;color:#3a3a44}
.quote .who{position:absolute;left:26px;top:247px;font-size:14px;font-weight:700;color:var(--ink)}
.quote .who small{font-size:11.5px;font-weight:400}
.quote .bar{position:absolute;left:0;bottom:0;width:100%;height:16px;background:var(--pink);clip-path:polygon(0 0,100% 100%,0 100%)}
.arrow{position:absolute;top:3038px;width:33px;height:33px;display:flex;align-items:center;justify-content:center}

/* footer */
.site-footer{position:absolute;left:0;top:3862px;width:1200px;height:324px;background:var(--purple)}
.f-col{position:absolute;top:3924px;color:var(--white)}
.f-col h4{font-size:14.5px;font-weight:700;text-transform:uppercase;margin-bottom:22px;position:relative}
.f-col h4::after{content:"";position:absolute;left:0;bottom:-8px;width:34px;height:2px;background:var(--pink)}
.f-col li{list-style:none;font-size:12.5px;line-height:26.5px}
.contact-row{display:flex;gap:14px;font-size:12.5px;line-height:20px;margin-bottom:21px}
.contact-row i{flex:none;width:26px;height:26px;border-radius:50%;background:#4a2f66;display:flex;align-items:center;justify-content:center}
</style>
</head>
<body>
<div class="page">

  <!-- HEADER -->
  <header class="site-header">
    <div class="brand" style="left:143px;top:36px;font-size:15px">
      <span class="brand-square" style="width:34px;height:34px"></span>Amber Crest Dispensing
    </div>
    <div class="social" style="left:660px;top:25px"><span></span><span></span><span></span></div>
    <a class="btn" href="#" style="left:798px;top:20px;width:108px;height:42px;font-size:14px">Sign Up</a>
    <nav class="nav">
      <a class="active" href="#">Home</a><a href="#">Services</a><a href="#">Our Machines</a><a href="#">For Businesses</a><a href="#">Request a Refund</a><a href="#">Support</a><a href="#">Contact Us</a>
    </nav>
    <div class="call-box"></div>
    <svg class="abs" style="left:1077px;top:26px" width="28" height="28" viewBox="0 0 28 28" aria-hidden="true">
      <circle cx="14" cy="14" r="14" fill="#ffffff"/>
      <path d="M9 8c1-1 2 0 3 2s0 2-1 3c1 2 2 3 4 4 1-1 1-2 3-1s3 2 2 3c-1 2-3 3-6 1-3-2-5-4-6-7-1-2 0-4 1-5z" fill="#ec3a8e"/>
    </svg>
    <div class="abs" style="left:1119px;top:31px;color:#fff;font-size:14px;font-weight:500">Call Us:</div>
    <div class="abs" style="left:980px;top:66px;color:#fff;font-size:21px;font-weight:700">+1 (555) 271-0962</div>
  </header>

  <!-- HERO -->
  <section>
    <div class="hero-photo" role="img" aria-label="Photo of a woman paying by phone at a modern glass-front smart vending machine in an office"></div>
    <div class="hero-shade"></div>
    <h1 class="hero-title">Smarter Snacks<br>for Today's Workplace</h1>
    <p class="hero-sub">Modern Vending &amp; Smart Micro-Market Solutions Reliable, Fully<br>Managed Vending Services for Local Businesses</p>
    <a class="btn" href="#" style="left:530px;top:465px;width:138px;height:42px;font-size:14px">Get Started</a>
    <div class="dots">
      <span style="top:547px"></span><span class="on" style="top:575px"></span><span style="top:604px"></span><span style="top:633px"></span>
    </div>
    <svg class="abs" style="left:0;top:600px" width="1200" height="175" viewBox="0 0 1200 175" aria-hidden="true">
      <polygon points="0,175 300,26 1200,150 1200,175" fill="#ffffff"/>
      <polygon points="300,18 1200,118 1200,150 300,38" fill="#ec3a8e"/>
    </svg>
  </section>

  <!-- ABOUT -->
  <section>
    <svg class="abs" style="left:899px;top:813px" width="160" height="448" viewBox="0 0 160 448" aria-hidden="true">
      <polygon points="60,0 160,0 0,170 0,110" fill="#f1f1f1"/>
      <polygon points="160,240 160,310 0,448 0,380" fill="#f1f1f1"/>
      <polygon points="0,120 150,0 150,160 0,300" fill="#f4f4f4"/>
    </svg>
    <div class="abs" style="left:104px;top:976px;width:332px;height:296px;border:8px solid var(--pink)"></div>
    <div class="abs" style="left:112px;top:984px;width:210px;height:20px;background:#fff"></div>
    <div class="photo" style="left:177px;top:811px;width:273px;height:308px;background:linear-gradient(160deg,#6f7f78,#a8927d 55%,#4d5a58)" role="img" aria-label="Photo of a smiling woman stocking a vending machine"></div>
    <div class="photo" style="left:328px;top:969px;width:204px;height:228px;background:linear-gradient(180deg,#4a4a4e,#6b6560 60%,#3a3836);border:3px solid #fff" role="img" aria-label="Photo of a stocked vending machine in a modern office kitchen"></div>
    <h2 class="heading abs" style="left:600px;top:830px;font-size:42px">About Us</h2>
    <div class="underline" style="left:600px;top:883px;width:108px"></div>
    <p class="about-text" style="top:914px">We specialize in providing comprehensive vending solutions tailored to your specific location. Whether you're looking to stock your office, school, or business with snacks, beverages, or other essentials, we've got you covered.</p>
    <p class="about-text" style="top:1020px">Amber Crest Dispensing provides modern vending machines and mini markets designed to keep employees, customers, and guests satisfied — without any hassle for your business. We supply, install, stock, and maintain state-of-the-art machines featuring tap-to-pay technology, cashless options, and a wide variety of snacks, drinks, and fresh food — all at no cost to your business.</p>
    <a class="btn" href="#" style="left:600px;top:1185px;width:140px;height:48px">Learn More</a>
  </section>

  <!-- MACHINES -->
  <section>
    <div class="machines"></div>
    <h2 class="heading abs" style="left:0;top:1430px;width:1200px;text-align:center;font-size:42px">Our Vending Machines</h2>
    <div class="underline" style="left:544px;top:1485px;width:108px"></div>

    <article class="card" style="left:143px;width:283px">
      <div class="machine" style="background:linear-gradient(180deg,#1e1e22,#3a2a2a 50%,#1e1e22)" role="img" aria-label="Photo of a black snack vending machine"></div>
      <h3>Snack Machines</h3>
      <p>Snack vending machines provide the convenience of quick and easy access to snacks at any time of day or night, without the need to leave your current location</p>
      <span class="go"><svg width="10" height="12" viewBox="0 0 10 12"><path d="M2 1l5 5-5 5" stroke="#ec3a8e" stroke-width="2" fill="none"/></svg></span>
    </article>
    <article class="card featured" style="left:457px;width:286px">
      <div class="machine" style="background:linear-gradient(180deg,#9aa4ad,#2e6ab8 60%,#1d4c8c)" role="img" aria-label="Photo of a glass-front drink vending machine"></div>
      <h3>Drink Machines</h3>
      <p>Drink vending machines provide the convenience of offering your business patrons quick, easy access to a wide variety of cold beverage option.</p>
      <span class="go"><svg width="10" height="12" viewBox="0 0 10 12"><path d="M2 1l5 5-5 5" stroke="#ffffff" stroke-width="2" fill="none"/></svg></span>
    </article>
    <article class="card" style="left:772px;width:283px">
      <div class="machine" style="background:linear-gradient(180deg,#6b7078,#3f4d6a 55%,#3a78c8)" role="img" aria-label="Photo of a combination snack and drink vending machine"></div>
      <h3>Combonation Machines</h3>
      <p>Combo vending machines are convenient because they offer a wide selection of snacks and drinks in one place. They are a good choice for locations</p>
      <span class="go"><svg width="10" height="12" viewBox="0 0 10 12"><path d="M2 1l5 5-5 5" stroke="#ec3a8e" stroke-width="2" fill="none"/></svg></span>
    </article>
    <div class="more-machines">
      <strong>Also available:</strong><span>Cold Food Machines</span><span>Coffee Machines</span><span>Mini Markets</span>
    </div>
  </section>

  <!-- BENEFITS -->
  <section>
    <div class="benefits" role="img" aria-label="Faint photo of an office break room behind a purple overlay"></div>
    <h2 class="heading abs" style="left:0;top:2153px;width:1200px;text-align:center;font-size:42px;line-height:47px;color:#fff">The Benefits of Smart<br>Vending Services</h2>
    <div class="underline" style="left:544px;top:2259px;width:108px"></div>

    <div class="hex" style="left:143px">
      <svg class="shape" width="213" height="244" viewBox="0 0 213 244"><polygon points="106.5,0 213,61 213,183 106.5,244 0,183 0,61" fill="#fff"/></svg>
      <svg class="icon" width="60" height="60" viewBox="0 0 60 60" aria-hidden="true">
        <polygon points="30,2 33,9 40,9 34,13 36,20 30,16 24,20 26,13 20,9 27,9" fill="#ec3a8e"/>
        <polygon points="12,8 14,13 19,13 15,16 17,21 12,18 7,21 9,16 5,13 10,13" fill="#ec3a8e"/>
        <polygon points="48,8 50,13 55,13 51,16 53,21 48,18 43,21 45,16 41,13 46,13" fill="#ec3a8e"/>
        <circle cx="30" cy="30" r="7" fill="#32194d"/><circle cx="13" cy="33" r="6" fill="#32194d"/><circle cx="47" cy="33" r="6" fill="#32194d"/>
        <path d="M18 58c0-12 5-18 12-18s12 6 12 18z" fill="#32194d"/>
        <path d="M2 56c0-10 4-15 11-15 3 0 5 1 6 3-2 3-3 7-3 12z" fill="#32194d"/>
        <path d="M58 56c0-10-4-15-11-15-3 0-5 1-6 3 2 3 3 7 3 12z" fill="#32194d"/>
      </svg>
      <div class="label">Increases Employee and Customer Satisfaction</div>
    </div>
    <div class="hex" style="left:378px">
      <svg class="shape" width="213" height="244" viewBox="0 0 213 244"><polygon points="106.5,0 213,61 213,183 106.5,244 0,183 0,61" fill="#fff"/></svg>
      <svg class="icon" width="60" height="60" viewBox="0 0 60 60" aria-hidden="true">
        <rect x="8" y="10" width="20" height="46" rx="2" fill="#ec3a8e"/><rect x="6" y="8" width="24" height="6" fill="#ec3a8e"/>
        <path d="M18 8l4-8" stroke="#ec3a8e" stroke-width="3"/>
        <path d="M24 36a18 14 0 0 1 34 0z" fill="#32194d"/><rect x="24" y="40" width="34" height="5" fill="#32194d"/><rect x="24" y="48" width="34" height="8" rx="3" fill="#32194d"/>
      </svg>
      <div class="label">Provides Convenient, On-Site Food and Drink Options</div>
    </div>
    <div class="hex active" style="left:611px">
      <svg class="shape" width="213" height="244" viewBox="0 0 213 244"><polygon points="106.5,0 213,61 213,183 106.5,244 0,183 0,61" fill="#ec3a8e"/></svg>
      <svg class="icon" width="60" height="60" viewBox="0 0 60 60" aria-hidden="true">
        <circle cx="38" cy="18" r="14" fill="none" stroke="#fff" stroke-width="3"/>
        <text x="38" y="24" text-anchor="middle" font-family="Roboto,Arial,sans-serif" font-size="17" font-weight="700" fill="#fff">$</text>
        <rect x="2" y="38" width="10" height="18" fill="#fff"/>
        <path d="M14 40h14c4 0 5 4 1 5h-8M14 54h22l20-12c3-2 0-6-3-4l-13 7" fill="none" stroke="#fff" stroke-width="3"/>
      </svg>
      <div class="label">No Upfront Cost or Equipment Fees</div>
    </div>
    <div class="hex" style="left:845px">
      <svg class="shape" width="213" height="244" viewBox="0 0 213 244"><polygon points="106.5,0 213,61 213,183 106.5,244 0,183 0,61" fill="#fff"/></svg>
      <svg class="icon" width="60" height="60" viewBox="0 0 60 60" aria-hidden="true">
        <g fill="#32194d"><rect x="26" y="0" width="8" height="10"/><rect x="26" y="50" width="8" height="10"/><rect x="0" y="26" width="10" height="8"/><rect x="50" y="26" width="10" height="8"/>
        <rect x="26" y="0" width="8" height="10" transform="rotate(45 30 30)"/><rect x="26" y="50" width="8" height="10" transform="rotate(45 30 30)"/><rect x="0" y="26" width="10" height="8" transform="rotate(45 30 30)"/><rect x="50" y="26" width="10" height="8" transform="rotate(45 30 30)"/>
        <circle cx="30" cy="30" r="22"/></g>
        <rect x="16" y="21" width="28" height="18" rx="2" fill="#fff"/><rect x="16" y="25" width="28" height="4" fill="#ec3a8e"/><rect x="20" y="32" width="10" height="3" fill="#32194d"/>
      </svg>
      <div class="label">Cashless, Contactless Payment Options</div>
    </div>
    <a class="btn" href="#" style="left:530px;top:2577px;width:138px;height:46px">Contact Us</a>
    <svg class="abs" style="left:0;top:2590px" width="1200" height="195" viewBox="0 0 1200 195" aria-hidden="true">
      <polygon points="0,0 560,60 0,190" fill="#ec3a8e"/>
      <polygon points="0,190 1200,60 1200,195 0,195" fill="#ffffff"/>
    </svg>
  </section>

  <!-- TESTIMONIALS -->
  <section>
    <h2 class="heading abs" style="left:0;top:2797px;width:1200px;text-align:center;font-size:42px">Testimonials</h2>
    <div class="underline" style="left:544px;top:2854px;width:108px"></div>
    <div class="arrow" style="left:65px;background:#ebe8ef"><svg width="10" height="14" viewBox="0 0 10 14"><path d="M8 1L2 7l6 6" stroke="#32194d" stroke-width="2" fill="none"/></svg></div>
    <div class="arrow" style="left:1103px;background:var(--pink)"><svg width="10" height="14" viewBox="0 0 10 14"><path d="M2 1l6 6-6 6" stroke="#fff" stroke-width="2" fill="none"/></svg></div>

    <article class="quote" style="left:143px">
      <div class="stars">★★★★★</div>
      <p>Lorem ipsum dolor sit amet, consectetur adipiscing elit, sed do eiusmod tempor incididunt ut labore et dolore magna aliqua. Ut enim ad minim veniam, quis nostrud exercitation ullamco laboris nisi ut aliquip ex ea commodo consequat.</p>
      <div class="who">- ALEX MARLOW, <small>United States</small></div>
      <div class="bar"></div>
    </article>
    <article class="quote" style="left:460px">
      <div class="stars">★★★★★</div>
      <p>Lorem ipsum dolor sit amet, consectetur adipiscing elit, sed do eiusmod tempor incididunt ut labore et dolore magna aliqua. Ut enim ad minim veniam, quis nostrud exercitation ullamco laboris nisi ut aliquip ex ea commodo consequat.</p>
      <div class="who">- ALEX MARLOW, <small>United States</small></div>
      <div class="bar"></div>
    </article>
    <article class="quote" style="left:776px">
      <div class="stars">★★★★★</div>
      <p>Lorem ipsum dolor sit amet, consectetur adipiscing elit, sed do eiusmod tempor incididunt ut labore et dolore magna aliqua. Ut enim ad minim veniam, quis nostrud exercitation ullamco laboris nisi ut aliquip ex ea commodo consequat.</p>
      <div class="who">- ALEX MARLOW, <small>United States</small></div>
      <div class="bar"></div>
    </article>
  </section>

  <!-- CALL TO ACTION -->
  <section>
    <svg class="abs" style="left:0;top:3301px" width="1200" height="561" viewBox="0 0 1200 561" aria-hidden="true">
      <polygon points="0,162 602,0 602,561 0,561" fill="#f1eef5"/>
    </svg>
    <div class="abs" style="left:602px;top:3301px;width:598px;height:561px;background:linear-gradient(110deg,#3c3a3f 0%,#8b8379 45%,#c9c0b4 80%,#e4ddd3 100%);clip-path:polygon(0 0,100% 17%,100% 100%,0 100%)" role="img" aria-label="Photo of a woman with glasses and a coffee cup choosing from a vending machine"></div>
    <h2 class="heading abs" style="left:143px;top:3500px;font-size:36px;line-height:44px;font-weight:500">Ready to Add<br>Vending to Your<br>Business?</h2>
    <p class="abs" style="left:143px;top:3671px;width:430px;font-size:15px;line-height:26px;color:#2c2c36">Let Amber Crest Dispensing handle everything — so you can focus on running your business.</p>
    <a class="btn" href="#" style="left:143px;top:3743px;width:183px;height:45px;font-size:14.5px">Contact Us Today</a>
  </section>

  <!-- FOOTER -->
  <footer>
    <div class="site-footer"></div>
    <div class="brand" style="left:143px;top:3990px;font-size:14px;color:#fff">
      <span class="brand-square" style="width:30px;height:30px"></span>Amber Crest Dispensing
    </div>
    <div class="f-col" style="left:437px">
      <h4>Quick Links</h4>
      <ul><li>Home</li><li>Services</li><li>Our Machines</li><li>For Businesses</li><li>Support</li><li>Contact Us</li></ul>
    </div>
    <div class="f-col" style="left:611px">
      <h4>Quick Links</h4>
      <ul><li>Privacy Policy</li><li>Terms &amp; Conditions</li><li>Legal Support</li><li>Disclaimer</li></ul>
    </div>
    <div class="f-col" style="left:797px;width:290px">
      <h4>Contact Info</h4>
      <div class="contact-row" style="margin-top:2px"><i><svg width="12" height="12" viewBox="0 0 12 12"><path d="M2 1c1-1 2 0 2 1s0 2-1 2c1 2 2 3 4 4 0-1 1-1 2-1s2 1 1 2c-1 2-3 2-5 0S0 4 2 1z" fill="#ec3a8e"/></svg></i><span>+1 (555) 271-0962</span></div>
      <div class="contact-row"><i><svg width="12" height="10" viewBox="0 0 12 10"><rect x="0" y="0" width="12" height="10" rx="1" fill="#ec3a8e"/><path d="M0 1l6 5 6-5" stroke="#4a2f66" stroke-width="1.2" fill="none"/></svg></i><span>ambercrestdispensing@mailnook.com</span></div>
      <div class="contact-row"><i><svg width="10" height="13" viewBox="0 0 10 13"><path d="M5 13S0 7 0 5a5 5 0 0 1 10 0c0 2-5 8-5 8z" fill="#ec3a8e"/><circle cx="5" cy="5" r="2" fill="#4a2f66"/></svg></i><span>123, Amber Crest Dispensing, Lorum Ipsum<br>United States</span></div>
    </div>
    <div class="abs" style="left:143px;top:4122px;width:914px;height:1px;background:#4d3568"></div>
    <div class="abs" style="left:0;top:4143px;width:1200px;text-align:center;color:#fff;font-size:11.5px">© 2026 &nbsp;/&nbsp; All Rights Reserved</div>
    <div class="abs" style="left:948px;top:4136px;display:flex;gap:9px">
      <span style="width:31px;height:31px;background:var(--pink);clip-path:polygon(50% 0,100% 25%,100% 75%,50% 100%,0 75%,0 25%)"></span>
      <span style="width:31px;height:31px;background:#fff;clip-path:polygon(50% 0,100% 25%,100% 75%,50% 100%,0 75%,0 25%)"></span>
      <span style="width:31px;height:31px;background:#fff;clip-path:polygon(50% 0,100% 25%,100% 75%,50% 100%,0 75%,0 25%)"></span>
    </div>
  </footer>

</div>
</body>
</html>
```